Letterhead design for business

Looking for an attractive and professional letterhead that uses the logo that is attached below.

Target Market(s)

Potential bankruptcy clients.

Industry/Entity Type

Legal

Colors

Designer to choose colors to be used in the design.

Requirements
Must have
• Address for locations, phone number, and website address.
• Addresses are on website ferncoveadvice.example. Use following phone number (for tracking purposes): 555-013-8274

```html
<!DOCTYPE html>
<html lang="en">
<head>
<meta charset="utf-8">
<title>Ferncove Law Group Letterhead</title>
<link rel="stylesheet" href="https://fonts.googleapis.com/css2?family=Open+Sans:wght@400;600&family=Arimo&display=swap">
<style>
  :root {
    --green: #7fbf86;
    --charcoal: #3a3a3c;
    --ink: #444446;
    --paper: #ffffff;
  }
  * { margin: 0; padding: 0; box-sizing: border-box; }
  html, body { width: 1040px; height: 1200px; overflow: hidden; background: var(--paper); }
  .letterhead {
    position: relative; width: 1040px; height: 1200px;
    font-family: "Open Sans", sans-serif; color: var(--ink);
  }
  .side-band { position: absolute; left: 0; top: 0; }
  .brand {
    position: absolute; left: 683px; top: 42px; width: 300px;
    text-align: center;
  }
  .brand-dot {
    width: 100px; height: 100px; border-radius: 50%;
    background: var(--green); margin: 0 auto 46px;
  }
  .brand-name {
    font-size: 26px; font-weight: 400; color: var(--charcoal);
    line-height: 1.2; white-space: nowrap;
  }
  .block { position: absolute; left: 99px; width: 840px; font-size: 15px; line-height: 20px; }
  .issue-date { top: 216px; }
  .recipient { top: 252px; }
  .greeting { top: 356px; }
  .para { font-size: 15px; line-height: 27px; text-align: justify; }
  .para-1 { top: 406px; }
  .para-2 { top: 568px; }
  .para-3 { top: 676px; }
  .closing { top: 816px; }
  .signature-mark {
    position: absolute; left: 99px; top: 852px; width: 240px; height: 24px;
    background: linear-gradient(90deg, #e6e6e8, #f4f4f5); border-radius: 12px;
  }
  .signer-name { position: absolute; left: 99px; top: 890px; font-size: 20px; font-weight: 600; color: var(--charcoal); }
  .signer-title { position: absolute; left: 99px; top: 922px; font-size: 15px; }
  .footer { position: absolute; top: 1110px; font-family: "Arimo", sans-serif; font-size: 18px; color: #111; line-height: 26px; }
  .contact { left: 97px; }
  .locations { right: 96px; text-align: right; }
  .footer-line { display: flex; align-items: center; gap: 6px; white-space: nowrap; }
  .locations .footer-line { justify-content: flex-end; }
  .icon { width: 15px; height: 15px; flex: none; }
</style>
</head>
<body>
<main class="letterhead">
  <svg class="side-band" width="30" height="1200" viewBox="0 0 30 1200" aria-hidden="true">
    <polygon points="0,0 29,0 29,512 0,490" fill="var(--green)"/>
    <polygon points="0,510 29,534 29,1200 0,1200" fill="var(--charcoal)"/>
  </svg>

  <header class="brand">
    <div class="brand-dot"></div>
    <div class="brand-name">Ferncove Law Group</div>
  </header>

  <p class="block issue-date">Issuing Date: May 5, 2018</p>
  <p class="block recipient">Name Of Employee Mr. XYZABC<br>Address of Employee<br>Address Line 2 etc..</p>
  <p class="block greeting">Dear Mr.XYZABC</p>

  <p class="block para para-1">Lorem Ipsum has been the industry's standard dummy text ever since the 1500s, when an unknown printer took a galley of type and scrambled it to make a type specimen book. It has survived not only five centuries, but also the leap into electronic typesetting, remaining essentially unchanged. It was popularised in the 1960s with the release of Marrowline sheets containing Lorem Ipsum passages, and more recently with desktop publishing software like Quillset Studio including versions of Lorem Ipsum.</p>
  <p class="block para para-2">Lorem Ipsum is simply dummy text of the printing and typesetting industry. Lorem Ipsum has been the industry's standard dummy text ever since the 1500s, when an unknown printer took a galley of type and scrambled it to make a type specimen book.</p>
  <p class="block para para-3">It has survived not only five centuries, but also the leap into electronic typesetting, remaining essentially unchanged. It was popularised in the 1960s with the release of Marrowline sheets containing Lorem IpsumIpsum passages.</p>

  <p class="block closing">Yours Sincerely</p>
  <div class="signature-mark" role="img" aria-label="Handwritten signature of Jonathan Reed"></div>
  <p class="signer-name">Jonathan Reed</p>
  <p class="signer-title">Managing Director</p>

  <footer>
    <div class="footer contact">
      <div class="footer-line">
        <svg class="icon" viewBox="0 0 16 16" aria-hidden="true"><path d="M2 6c0-2 2-3 6-3s6 1 6 3v1h-3V6H5v1H2z M4 8h8l1 5H3z" fill="var(--green)"/></svg>
        <span>555-013-8274</span>
      </div>
      <div class="footer-line">
        <svg class="icon" viewBox="0 0 16 16" aria-hidden="true"><circle cx="8" cy="8" r="7" fill="var(--green)"/><path d="M4 6c2 0 3 1 3 3s2 2 2 4M10 3c0 2 2 2 3 3" stroke="#fff" stroke-width="1.4" fill="none"/></svg>
        <span>www.ferncoveadvice.example</span>
      </div>
    </div>
    <div class="footer locations">
      <div class="footer-line">
        <span>418 Linden Ave., Suite #1200 Marlow Georgia 30999</span>
        <svg class="icon" viewBox="0 0 16 16" aria-hidden="true"><path d="M8 1a5 5 0 0 0-5 5c0 4 5 9 5 9s5-5 5-9a5 5 0 0 0-5-5z" fill="var(--green)"/><circle cx="8" cy="6" r="2" fill="#fff"/></svg>
      </div>
      <div class="footer-line">
        <span>5120 W. Harbor St. Elmstead Georgia 30998</span>
        <svg class="icon" viewBox="0 0 16 16" aria-hidden="true"><path d="M8 1a5 5 0 0 0-5 5c0 4 5 9 5 9s5-5 5-9a5 5 0 0 0-5-5z" fill="var(--green)"/><circle cx="8" cy="6" r="2" fill="#fff"/></svg>
      </div>
    </div>
  </footer>
</main>
</body>
</html>
```